Restaurant needs a vertical banner for fried catfish

Our restaurant is looking for an eye-catching 78.75in. x 36in. vertical physical banner ad for our fried catfish. Photos for the fried catfish will be provided as a reference but we will also accept anything similar to the photo. We will be using the following as our receptacle: https://www.plankoria.example/banner-stand/retractable-banner-stands/
The design must incorporate the following flavor texts:
Fried Catfish
Always Fresh!
Made from Scratch
Hand-cut Fillets
The Best Catfish in Texas
Served with fries, hush puppies, and a 32oz fountain drink
Also available by the pound!
The final design should be creative, professional, and eye-catching for customers.
Updates
Colors
Designer to choose colors to be used in the design.
Requirements
Must have
- We are open to any and all design elements, albeit the 'flavor texts' should not overpower, but complement the fried catfish photo. 'Fried Catfish' can be used in lieu of a main title/logo.
Nice to have
- Transparent or textured backgrounds that can encompass any or all part of the banner such as a cutting board, shadows, abstract, etc to show depth are a plus.
- Use of vectors or objects such as ribbons or shapes to encapsulate the 'flavor texts' are also encouraged.

```html
<!DOCTYPE html>
<html lang="en">
<head>
<meta charset="utf-8">
<title>Fried Catfish Banner</title>
<link href="https://fonts.googleapis.com/css2?family=Archivo+Black&family=Chewy&family=Montserrat:wght@400;700;800&display=swap" rel="stylesheet">
<style>
  :root {
    --orange: #ee5a1e;
    --orange-light: #f3782a;
    --orange-deep: #e2401c;
    --amber: #f28c10;
    --brown: #5b2914;
    --brown-dark: #3f1c0c;
    --white: #ffffff;
  }
  * { margin: 0; padding: 0; box-sizing: border-box; }
  html, body { width: 1200px; height: 2627px; overflow: hidden; background: var(--white); }
  .canvas { position: relative; width: 1200px; height: 2627px; background: var(--white); }
  .banner {
    position: absolute; left: 175px; top: 382px; width: 844px; height: 1846px;
    background: radial-gradient(ellipse at 60% 20%, var(--orange-light) 0%, var(--orange) 45%, var(--orange-deep) 100%);
    overflow: hidden;
  }
  .title { font-weight: 400; font-size: 0; }
  .title-fried {
    position: absolute; left: 0; top: 50px; width: 844px;
    font-family: 'Chewy', cursive; font-weight: 400; font-size: 230px; line-height: 1;
    color: var(--white); text-align: center; white-space: nowrap;
  }
  .title-catfish {
    position: absolute; left: 0; top: 300px; width: 844px;
    font-family: 'Archivo Black', sans-serif; font-weight: 400; font-size: 146px; line-height: 1;
    color: var(--white); text-align: center; letter-spacing: -2px; white-space: nowrap;
  }
  .photo { position: absolute; left: 0; top: 480px; width: 844px; height: 800px; }
  .features {
    position: absolute; left: 83px; top: 1301px; width: 740px;
    list-style: none;
    display: grid; grid-template-columns: 319px 1fr; row-gap: 26px;
  }
  .feature { display: flex; align-items: flex-start; gap: 8px; }
  .feature svg { flex: none; width: 54px; height: 54px; margin-top: 4px; }
  .feature span {
    font-family: 'Montserrat', sans-serif; font-weight: 800; font-size: 32px;
    line-height: 0.98; color: var(--brown); text-transform: uppercase;
    letter-spacing: -1px; white-space: nowrap;
  }
  .served-title {
    position: absolute; left: 0; top: 1522px; width: 844px; text-align: center;
    font-family: 'Archivo Black', sans-serif; font-weight: 400; font-size: 92px; line-height: 1;
    color: var(--white); letter-spacing: 2px; white-space: nowrap;
  }
  .served-items {
    position: absolute; left: 0; top: 1618px; width: 844px; text-align: center;
    font-family: 'Montserrat', sans-serif; font-weight: 400; font-size: 36px;
    line-height: 1.15; color: var(--white); text-transform: uppercase;
  }
  .by-pound {
    position: absolute; left: 199px; top: 1735px; width: 447px; height: 111px;
    background: var(--amber); border-radius: 18px 18px 0 0;
    display: flex; align-items: center; justify-content: center; text-align: center;
    font-family: 'Archivo Black', sans-serif; font-size: 35px; line-height: 0.95;
    color: var(--brown-dark); text-transform: uppercase; letter-spacing: 1px;
  }
</style>
</head>
<body>
<div class="canvas">
  <section class="banner">
    <h1 class="title">
      <span class="title-fried">FRIED</span>
      <span class="title-catfish">CATFISH</span>
    </h1>

    <svg class="photo" viewBox="0 0 844 800" role="img" aria-label="Plate of golden cornmeal-crusted catfish fillets with french fries and hush puppies">
      <defs>
        <linearGradient id="plate-tones" x1="0" y1="0" x2="1" y2="1">
          <stop offset="0" stop-color="#d9a35a"/>
          <stop offset="0.45" stop-color="#b8742e"/>
          <stop offset="0.8" stop-color="#e7c07a"/>
          <stop offset="1" stop-color="#f1ece2"/>
        </linearGradient>
      </defs>
      <path d="M0 118 Q420 -10 844 22 L844 52 Q420 20 0 148 Z" fill="var(--brown)"/>
      <path d="M0 148 Q420 20 844 52 L844 690 Q560 800 300 735 Q130 690 0 640 Z" fill="url(#plate-tones)"/>
      <path d="M0 640 Q130 690 300 735 Q560 800 844 690 L844 718 Q560 830 300 764 Q130 720 0 668 Z" fill="var(--brown)"/>
    </svg>

    <ul class="features">
      <li class="feature">
        <svg viewBox="0 0 56 56"><path d="M4 4 H52 V36 L28 54 L4 36 Z" fill="var(--amber)"/><path d="M14 26 L25 37 L43 16" fill="none" stroke="var(--white)" stroke-width="5" stroke-linecap="round" stroke-linejoin="round"/></svg>
        <span>Made from<br>Scratch</span>
      </li>
      <li class="feature">
        <svg viewBox="0 0 56 56"><path d="M4 4 H52 V36 L28 54 L4 36 Z" fill="var(--amber)"/><path d="M14 26 L25 37 L43 16" fill="none" stroke="var(--white)" stroke-width="5" stroke-linecap="round" stroke-linejoin="round"/></svg>
        <span>Hand-cut<br>Fillets</span>
      </li>
      <li class="feature">
        <svg viewBox="0 0 56 56"><path d="M4 4 H52 V36 L28 54 L4 36 Z" fill="var(--amber)"/><path d="M14 26 L25 37 L43 16" fill="none" stroke="var(--white)" stroke-width="5" stroke-linecap="round" stroke-linejoin="round"/></svg>
        <span>Always<br>Fresh!</span>
      </li>
      <li class="feature">
        <svg viewBox="0 0 56 56"><path d="M4 4 H52 V36 L28 54 L4 36 Z" fill="var(--amber)"/><path d="M14 26 L25 37 L43 16" fill="none" stroke="var(--white)" stroke-width="5" stroke-linecap="round" stroke-linejoin="round"/></svg>
        <span>The best catfish<br>in Texas</span>
      </li>
    </ul>

    <h2 class="served-title">SERVED WITH</h2>
    <p class="served-items">Fries, hush puppies, and<br>a 32oz fountain drink</p>

    <div class="by-pound">Also available<br>by the pound!</div>
  </section>
</div>
</body>
</html>
```